Update Financial Planning Presentation

We currently use a stock Powerpoint template. Information is imputed into an Excel spreadsheet and then linked to the presentation. We are looking to improve and upgrade this to a more straightforward and "cleaner" looking template. I have attached a sample copy of the Powerpoint presantation we currently use along with the Excel spreadsheet. I have attached our logo as well. Thanks.
Industry/Entity Type
Financial

```html
<!DOCTYPE html>
<html lang="en">
<head>
<meta charset="utf-8">
<title>Brightfield Financial – Presentation Template</title>
<link href="https://fonts.googleapis.com/css2?family=Lora:ital,wght@0,400;0,700;1,400&display=swap" rel="stylesheet">
<style>
:root{
  --board:#626265;
  --paper:#ffffff;
  --ink:#111111;
  --brand:#3c9a45;
  --band:#5ea85e;
  --row-green:#1f8a3a;
  --row-black:#070707;
  --bar-light:#5daa60;
  --bar-bright:#23a84a;
  --bar-grey:#555555;
  --tree:#a8c88a;
}
*{margin:0;padding:0;box-sizing:border-box}
html,body{width:1200px;height:924px;overflow:hidden;background:var(--board);font-family:'Lora',serif;color:var(--ink)}
.slide{position:absolute;width:492px;height:368px;background:var(--paper);box-shadow:6px 7px 8px rgba(0,0,0,.55);overflow:hidden}
.s1{left:83px;top:70px}.s2{left:620px;top:70px;width:502px;height:374px}
.s3{left:83px;top:487px}.s4{left:620px;top:485px;width:502px;height:375px}
.band{position:absolute;left:0;right:0;bottom:0;height:14px;background:var(--band)}
.s4 .band{height:28px;color:#fff;font-size:11px;text-align:center;line-height:42px}
.page-no{position:absolute;right:17px;top:0;width:28px;height:32px;background:#000;color:#fff;font-size:9px;text-align:center;line-height:32px}
.brand{position:absolute;left:14px;top:40px;display:flex;align-items:center;gap:4px;font-weight:700;font-size:11px;color:var(--brand)}
.brand-mark{width:7px;height:7px;background:var(--ink)}
.tree{position:absolute;right:6px;bottom:16px;width:64px;height:70px;border-radius:50% 50% 20% 20%;background:radial-gradient(circle at 50% 35%,#cfe0b4,var(--tree) 60%,#8fb46b)}
.title{position:absolute;left:0;right:0;top:58px;text-align:center;font-style:italic;font-size:17px}
/* timeline */
.chart{position:absolute;left:22px;top:100px}
.age-table{position:absolute;left:279px;top:187px;font-size:10px;line-height:11px;width:168px}
.age-table div{display:flex;justify-content:space-between}
/* planning table */
.plan{position:absolute;left:74px;top:88px;border-collapse:collapse;font-size:7.5px;width:318px}
.plan th{font-weight:700;text-align:center;padding:0 2px;height:11px}
.plan th:first-child{text-align:left}
.plan td{height:11.7px;padding:0 2px;color:#fff;border:1px solid #fff}
.plan td+td{text-align:center;width:40px}
.plan tr.g td{background:var(--row-green)}
.plan tr.b td{background:var(--row-black)}
.plan td.pl{width:38px}
.total{position:absolute;left:338px;top:297px;font-size:7.5px;width:54px;text-align:right}
.notes{position:absolute;left:74px;top:314px;font-size:6.5px;line-height:8px}
.hnote{position:absolute;left:282px;top:305px;font-size:6.5px;line-height:8px;width:110px}
/* services */
.services{position:absolute;left:90px;right:90px;top:56px;text-align:center;font-size:6.6px;line-height:8.8px}
.services .gap{height:9px}
.services strong{font-size:7px}
/* thanks */
.s4 .brand{left:0;right:0;top:94px;justify-content:center;font-size:20px}
.s4 .brand-mark{width:10px;height:10px}
.thanks{position:absolute;left:0;right:0;top:164px;text-align:center;font-size:16px}
.contact{position:absolute;left:0;right:0;top:246px;text-align:center;font-size:9.5px;line-height:18px}
</style>
</head>
<body>

<section class="slide s1">
  <div class="page-no">9</div>
  <div class="brand"><span class="brand-mark"></span>Brightfield Financial</div>
  <h1 class="title">Timeline</h1>
  <svg class="chart" width="200" height="160" viewBox="0 0 200 160" font-family="Lora, serif" font-size="7">
    <polygon points="15,12 22,5 22,95 15,102" fill="#888"/>
    <rect x="22" y="22" width="55" height="15" fill="var(--bar-light)"/>
    <rect x="22" y="38" width="150" height="17" fill="#000"/>
    <rect x="22" y="55" width="105" height="14" fill="var(--bar-bright)"/>
    <rect x="22" y="70" width="110" height="15" fill="var(--bar-grey)"/>
    <text x="84" y="30">30</text><text x="180" y="45">90</text><text x="133" y="63">60</text><text x="138" y="77">64</text>
    <line x1="15" y1="102" x2="182" y2="102" stroke="#999"/>
    <text x="13" y="116">0</text><text x="95" y="116">50</text><text x="177" y="116">100</text>
    <rect x="0.5" y="125" width="182" height="28" fill="none" stroke="#555" stroke-width=".7"/>
    <rect x="5" y="131" width="3" height="3" fill="var(--bar-light)"/><text x="11" y="135">Retirement Period</text>
    <rect x="96" y="131" width="3" height="3" fill="#000"/><text x="102" y="135">Joint Life Expectancy</text>
    <rect x="5" y="144" width="3" height="3" fill="var(--bar-bright)"/><text x="11" y="148">Retirement Age</text>
    <rect x="96" y="144" width="3" height="3" fill="var(--bar-grey)"/><text x="102" y="148">Youngest Age</text>
  </svg>
  <div class="age-table">
    <div><span>Current Age - Youngest</span><span>64</span></div>
    <div><span>Retirement Age</span><span>60</span></div>
    <div><span>Life Expectancy</span><span>90</span></div>
    <div><span>Retirement Period</span><span>30</span></div>
  </div>
  <div class="tree" role="img" aria-label="Illustrated green money tree"></div>
  <div class="band"></div>
</section>

<section class="slide s2">
  <div class="page-no">12</div>
  <div class="brand"><span class="brand-mark"></span>Brightfield Financial</div>
  <h1 class="title">Investment Planning</h1>
  <table class="plan">
    <tr><th>Risk &amp; Investments:</th><th>Risk</th><th>Horizon</th><th>Plan</th></tr>
    <tr class="g"><td>Term Deposits, GICs, T-Bills, Short Term Bonds</td><td>1</td><td>1 - 5</td><td class="pl">100%</td></tr>
    <tr class="g"><td>Deferred Annuities, CSBs, etc.</td><td>1</td><td>1 - 5</td><td class="pl"></td></tr>
    <tr class="b"><td>Dividend &amp; Income Funds</td><td>2</td><td>3 - 7</td><td class="pl"></td></tr>
    <tr class="b"><td>Balanced Funds</td><td>2</td><td>3 - 7</td><td class="pl"></td></tr>
    <tr class="g"><td>Long Term Bonds, Mortgage Backed Securities</td><td>3</td><td>4 - 10</td><td class="pl"></td></tr>
    <tr class="g"><td>International Balanced</td><td>3</td><td>4 - 10</td><td class="pl"></td></tr>
    <tr class="b"><td>International Bond</td><td>4</td><td>4 - 10</td><td class="pl"></td></tr>
    <tr class="b"><td>Canadian Equity - Large Cap.</td><td>4</td><td>5 - 10</td><td class="pl"></td></tr>
    <tr class="b"><td>Foreign Equity - Global Large Cap.</td><td>4</td><td>5 - 10</td><td class="pl"></td></tr>
    <tr class="g"><td>Canadian Equity - Small to Mid Cap.</td><td>5</td><td>6 - 10</td><td class="pl"></td></tr>
    <tr class="b"><td>Foreign Equity - European</td><td>6</td><td>7 - 10</td><td class="pl"></td></tr>
    <tr class="b"><td>Foreign Equity - USA &amp; North American</td><td>7</td><td>7 - 10</td><td class="pl"></td></tr>
    <tr class="g"><td>Specialty Funds</td><td>8</td><td>8 - 12</td><td class="pl"></td></tr>
    <tr class="g"><td>Labour Sponsored Funds</td><td>9</td><td>9 - 15</td><td class="pl"></td></tr>
    <tr class="g"><td>Asian &amp; Far East Equity</td><td>10</td><td>10 - 15</td><td class="pl"></td></tr>
    <tr class="g"><td>Emerging Markets - Latin America</td><td>10</td><td>10 - 15</td><td class="pl"></td></tr>
  </table>
  <div class="total">100.00%</div>
  <div class="hnote"><b>Horizon</b>: Investment Horizon in Years</div>
  <div class="notes"><b>Risk</b>: 1 = Least Risk; 10 = Most Risk<br><b>Plan</b>: Recommended Asset Allocation over the next five years<br>For illustration purposes only.</div>
  <div class="tree" role="img" aria-label="Illustrated green money tree"></div>
  <div class="band"></div>
</section>

<section class="slide s3">
  <div class="page-no">18</div>
  <div class="brand"><span class="brand-mark"></span>Brightfield Financial</div>
  <div class="services">
    Tax Planning<br>Deposit Broker<br>Life Insurance Agent<br>Certified Financial Planner<br>Mutual Fund Representative<br>Estate &amp; Retirement Planning
    <div class="gap"></div><div class="gap"></div>
    Group RRSPs, Pension Plans, Group Benefit Plans<br>Annuities, Life Insurance, Deferred Tax Plans<br>Term Deposits, Mutual Funds<br>Business Overhead Insurance<br>Accident &amp; Sickness Insurance<br>Registered Retirement Savings Plans<br>Registered Retirement Income Funds
    <div class="gap"></div>
    <strong>INDEPENDENT</strong>
    <div class="gap"></div>
    Representing Selected Canadian Financial Institutions
    <div class="gap"></div>
    Credit Unions, Trust Companies<br>Mutual Fund Companies<br>Life Insurance Companies
    <div class="gap"></div>
    <strong>OWEN R. HALE, CFP, CLU, CHFC<br>PETER R. HALE, CFP</strong>
    <div class="gap"></div>
    Brightfield Financial Services Ltd.: Life Insurance &amp; Financial Planning<br>Northgate Financial Security Investments Inc.: Mutual Funds<br>1200 Harbour Road, Westport BC V0X 1A0<br>Telephone: 555-010-0144; Fax: 555-010-0147<br>E-mail: info@brightfield.example
  </div>
  <div class="tree" role="img" aria-label="Illustrated green money tree"></div>
  <div class="band"></div>
</section>

<section class="slide s4">
  <div class="brand"><span class="brand-mark"></span>Brightfield Financial</div>
  <div class="thanks">Thank you</div>
  <div class="contact">Contact us: your Contact address<br>Your phone number and fax number<br>Comes here.</div>
  <div class="band">www.Yourwebid.com</div>
</section>

</body>
</html>
```